Derya & Kerem Wedding Invitation and Decorative Designs

We are looking for a sweet and elegant design for our wedding invitation. We need different versions of the same design to use both as printed hard copies and in digital formats (WhatsApp image, instagram post, etc) Please see attached sample invitation, which we like as a simple and elegant option, but also find it quite basic. We are open to creative suggestions following a similar style.
Once we decide on an invitation design, we would like to use the same design elements in guest name cards, welcome sign, menu cards and print cover for the dance floor of our wedding venue. Please see random samples of these materials attached. We also attach a photo from our wedding venue displaying a close to final visual of the decoration we chose for our wedding day (sharing in case it helps as an inspiration source and helps with matching decoration colors with the designs)
Requirements
Must have
- Must have a style similar to the attached sample invitation

```html
<!DOCTYPE html>
<html lang="en">
<head>
<meta charset="utf-8">
<title>Derya &amp; Kerem – Wedding Invitation</title>
<link rel="stylesheet" href="https://fonts.googleapis.com/css2?family=Pinyon+Script&family=Gabriela&family=Cormorant+Garamond:wght@500&display=swap">
<style>
  :root {
    --page: #ffffff;
    --frame: #ede0ea;
    --frame-edge: #e2cfdc;
    --lilac: #d0bdee;
    --lilac-deep: #b29bdb;
    --leaf: #a88fd3;
    --petal: #eee7fa;
    --plum: #6a4596;
    --outline: #5b4380;
    --ink: #1f1a22;
    --card: #f5eef3;
    --photo-a: #eadbe6;
    --photo-b: #b8a0b2;
  }
  * { margin: 0; padding: 0; box-sizing: border-box; }
  html, body { width: 1200px; height: 2400px; overflow: hidden; background: var(--page); }
  .canvas { position: relative; width: 1200px; height: 2400px; }

  .cover-card {
    position: absolute; left: 222px; top: 48px; width: 752px; height: 710px;
    background: var(--frame); border: 1px solid var(--frame-edge);
  }
  .cover-panel {
    position: absolute; left: 28px; top: 19px; width: 699px; height: 669px;
    background: var(--lilac);
    box-shadow: 0 2px 4px rgba(120, 90, 150, 0.25);
  }
  .floral-wreath {
    position: absolute; inset: 0;
    background:
      radial-gradient(circle at 50px 55px, var(--petal) 0 22px, transparent 48px),
      radial-gradient(circle at 645px 55px, var(--petal) 0 22px, transparent 48px),
      radial-gradient(circle at 50px 610px, var(--petal) 0 20px, transparent 46px),
      radial-gradient(circle at 645px 610px, var(--petal) 0 20px, transparent 46px),
      radial-gradient(circle at 535px 145px, var(--petal) 0 40px, transparent 80px),
      radial-gradient(circle at 175px 405px, var(--petal) 0 45px, transparent 88px),
      radial-gradient(circle at 545px 435px, var(--petal) 0 42px, transparent 84px),
      radial-gradient(circle at 255px 510px, var(--petal) 0 38px, transparent 78px),
      radial-gradient(circle at 425px 500px, var(--petal) 0 48px, transparent 92px),
      radial-gradient(ellipse 150px 300px at 120px 330px, var(--leaf), transparent 100%),
      radial-gradient(ellipse 150px 300px at 580px 330px, var(--leaf), transparent 100%),
      radial-gradient(ellipse 300px 120px at 350px 560px, var(--lilac-deep), transparent 100%);
    opacity: 0.9;
  }
  .invitation-arc { position: absolute; left: 205px; top: 35px; width: 290px; height: 110px; overflow: visible; }
  .invitation-arc text {
    font-family: "Cormorant Garamond", serif; font-weight: 500; font-size: 50px;
    fill: #fff; stroke: var(--outline); stroke-width: 2.4px; paint-order: stroke fill;
  }
  .cover-names {
    position: absolute; left: 0; width: 100%; top: 188px; text-align: center;
    font-family: "Pinyon Script", cursive; font-weight: 400; color: var(--plum);
    font-size: 88px; line-height: 96px;
  }
  .cover-names span { display: block; }
  .date-tab {
    position: absolute; left: 203px; top: 610px; width: 300px; height: 72px;
    background: var(--frame); border: 1px solid #efe5ec;
    font-family: "Cormorant Garamond", serif; font-weight: 500; color: var(--plum); font-size: 52px;
    font-variant-numeric: oldstyle-nums; text-align: center; line-height: 68px;
  }

  .detail-card {
    position: absolute; left: 227px; top: 832px; width: 752px; height: 1522px;
    background: var(--card);
  }
  .couple-photo {
    position: absolute; left: 0; top: 0; width: 752px; height: 743px;
    background: linear-gradient(160deg, var(--photo-a) 0%, #d6c2d1 45%, var(--photo-b) 100%);
  }
  .photo-mat {
    position: absolute; left: 35px; top: 28px; width: 689px; height: 688px;
    background: rgba(180,150,175,0.22);
  }
  .name-band {
    position: absolute; left: 0; top: 743px; width: 752px; height: 67px;
    background: var(--frame); border-top: 1px solid var(--frame-edge); border-bottom: 1px solid var(--frame-edge);
  }
  .detail-names {
    position: absolute; left: 76px; top: 826px;
    font-family: "Pinyon Script", cursive; font-weight: 400; color: var(--plum);
    font-size: 80px; line-height: 100px; white-space: nowrap;
  }
  .invite-message {
    position: absolute; left: 72px; top: 950px; width: 680px;
    font-family: "Gabriela", serif; color: var(--ink); font-size: 33px; line-height: 41px;
    letter-spacing: 4.5px; white-space: nowrap;
  }
  .date-band {
    position: absolute; left: 0; top: 1428px; width: 752px; height: 94px;
    background: var(--frame);
    font-family: "Cormorant Garamond", serif; font-weight: 500; color: var(--plum); font-size: 54px;
    font-variant-numeric: oldstyle-nums; text-align: center; line-height: 90px;
  }
</style>
</head>
<body>
<main class="canvas">
  <section class="cover-card">
    <div class="cover-panel">
      <div class="floral-wreath" role="img" aria-label="Watercolour wreath of pale lilac flowers and leaves"></div>
      <svg class="invitation-arc" viewBox="0 0 290 110" aria-label="Invitation">
        <path id="arc" d="M5 105 Q145 20 285 105" fill="none"/>
        <text><textPath href="#arc" startOffset="50%" text-anchor="middle">INVITATION</textPath></text>
      </svg>
      <h1 class="cover-names"><span>Derya</span><span>&amp; Kerem</span></h1>
      <div class="date-tab">April 30 2024</div>
    </div>
  </section>

  <section class="detail-card">
    <div class="couple-photo" role="img" aria-label="Soft lilac-toned photo of the couple embracing">
      <div class="photo-mat"></div>
    </div>
    <div class="name-band"></div>
    <h2 class="detail-names">Derya &amp; Kerem</h2>
    <p class="invite-message">We invite you to share with us<br>this moment of commitment<br>and loves in our life.</p>
    <div class="date-band">April 30 2024</div>
  </section>
</main>
</body>
</html>
```